Technical audit needs a report template

As our company runs various technical audits, we also provide findings on paper, online or in Powerpoint. For this reason we need an identity pack, which includes business cards, complimentary cards, letterhead and the likes.

Who would be up to create this stationery pack for us? We hope to receive a style for these documents, that look professional and can be easily extended.
Updates

Project Deadline Extended Reason: I would like to provide the opportunity to friended designers to submit their designs too! Added Sunday, October 9, 2016

Target Market(s)

Start-ups, scale-ups and investors

Industry/Entity Type

Investment

Contact Information for Business Card

Street: Kastelenhofweg 41
Postcode: 3614KT
City: Utrecht
Country: The Netherlands
Phone: +31 304185926
Cell Phone: +31 6 57193840
email: jorien@velmoraxis.example
website: https://velmoraxis.example

Requirements
Must have
• I don't have inspiration, should just be a slick design based on the logo provided.
Nice to have
• Logo could be on the back of the card?
Should not have
• Should not use different colours then the logo, or at least fit the colour scheme.

```html
<!DOCTYPE html>
<html lang="en">
<head>
<meta charset="utf-8">
<title>Velmoraxis – Business Card</title>
<link rel="stylesheet" href="https://fonts.googleapis.com/css2?family=Montserrat:wght@400;500;600;700&display=swap">
<style>
  :root {
    --bg: #e9e8e5;
    --card-white: #ffffff;
    --charcoal: #3b3c3f;
    --charcoal-deep: #2f3033;
    --blue: #1ba6d6;
    --blue-light: #39c1ea;
    --blue-deep: #1186b3;
    --ink: #333336;
    --grey-text: #6d6e71;
    --white: #ffffff;
  }
  * { box-sizing: border-box; margin: 0; padding: 0; }
  html, body {
    width: 1200px; height: 950px; overflow: hidden;
    background: var(--bg);
    font-family: "Montserrat", sans-serif;
  }
  .sheet { position: relative; width: 1200px; height: 950px; }
  .card {
    position: absolute; top: 115px; width: 420px; height: 720px;
    overflow: hidden; box-shadow: 0 6px 18px rgba(0,0,0,.18);
  }
  .card--front { left: 140px; background: var(--card-white); }
  .card--back { left: 640px; background: var(--charcoal); }
  .card__shapes { position: absolute; inset: 0; }

  .brand { position: absolute; left: 44px; top: 58px; display: flex; align-items: center; gap: 14px; }
  .brand__square { width: 34px; height: 34px; background: var(--blue); }
  .brand__name { font-weight: 600; font-size: 30px; letter-spacing: 1px; color: var(--ink); }

  .holder { position: absolute; left: 44px; top: 142px; }
  .holder__name { font-weight: 700; font-size: 22px; color: var(--blue); letter-spacing: .5px; }
  .holder__role { font-weight: 400; font-size: 15px; color: var(--grey-text); margin-top: 4px; }

  .contact { position: absolute; right: 34px; top: 480px; list-style: none; text-align: right; color: var(--white); font-size: 14px; font-weight: 500; line-height: 1.25; }
  .contact li { display: flex; justify-content: flex-end; align-items: flex-start; gap: 10px; margin-bottom: 10px; }
  .contact svg { width: 14px; height: 14px; flex: none; margin-top: 1px; }

  .back-brand { position: absolute; left: 44px; bottom: 88px; color: var(--white); }
  .back-brand__name { font-weight: 600; font-size: 40px; letter-spacing: 1.5px; }
  .back-brand__web { font-size: 14px; font-weight: 400; letter-spacing: 2px; margin-top: 8px; color: #d8d9db; }
</style>
</head>
<body>
<main class="sheet">

  <section class="card card--front" aria-label="Business card front">
    <svg class="card__shapes" viewBox="0 0 420 720" aria-hidden="true">
      <polygon points="0,318 120,408 420,238 420,262 120,432 0,342" fill="var(--blue)"/>
      <polygon points="0,342 120,432 420,262 420,276 120,446 0,356" fill="var(--blue-deep)"/>
      <polygon points="0,356 120,446 420,276 420,720 0,720" fill="var(--charcoal)"/>
    </svg>

    <div class="brand">
      <span class="brand__square"></span>
      <span class="brand__name">VELMORAXIS</span>
    </div>

    <div class="holder">
      <p class="holder__name">JORIEN VERMAAT</p>
      <p class="holder__role">CEO/Founder</p>
    </div>

    <ul class="contact">
      <li><span>+31 304185926</span>
        <svg viewBox="0 0 24 24"><path fill="var(--blue)" d="M6.6 10.8a15 15 0 0 0 6.6 6.6l2.2-2.2c.3-.3.7-.4 1-.2 1.1.4 2.3.6 3.6.6.6 0 1 .4 1 1V20c0 .6-.4 1-1 1A17 17 0 0 1 3 4c0-.6.4-1 1-1h3.5c.6 0 1 .4 1 1 0 1.3.2 2.5.6 3.6.1.3 0 .7-.2 1z"/></svg></li>
      <li><span>+31 6 57193840</span>
        <svg viewBox="0 0 24 24"><rect x="6" y="2" width="12" height="20" rx="2" fill="none" stroke="var(--blue)" stroke-width="2.4"/><circle cx="12" cy="18" r="1.3" fill="var(--blue)"/></svg></li>
      <li><span>+31 304185927</span>
        <svg viewBox="0 0 24 24"><rect x="3" y="5" width="18" height="12" rx="1" fill="none" stroke="var(--blue)" stroke-width="2.4"/><rect x="1" y="18" width="22" height="3" fill="var(--blue)"/></svg></li>
      <li><span>jorien@velmoraxis.example</span>
        <svg viewBox="0 0 24 24"><rect x="2" y="5" width="20" height="14" rx="1" fill="var(--blue)"/><path d="M2 6l10 7 10-7" fill="none" stroke="var(--charcoal)" stroke-width="1.8"/></svg></li>
      <li><span>velmoraxis.example</span>
        <svg viewBox="0 0 24 24"><circle cx="12" cy="12" r="9.5" fill="none" stroke="var(--blue)" stroke-width="2.2"/><path d="M2.5 12h19M12 2.5c3 3 3 16 0 19M12 2.5c-3 3-3 16 0 19" fill="none" stroke="var(--blue)" stroke-width="1.6"/></svg></li>
      <li><span>Kastelenhofweg 41<br>3614KT Utrecht</span>
        <svg viewBox="0 0 24 24"><path fill="var(--blue)" d="M12 2a7 7 0 0 0-7 7c0 5 7 13 7 13s7-8 7-13a7 7 0 0 0-7-7zm0 9.5A2.5 2.5 0 1 1 12 6.5a2.5 2.5 0 0 1 0 5z"/></svg></li>
    </ul>
  </section>

  <section class="card card--back" aria-label="Business card back">
    <svg class="card__shapes" viewBox="0 0 420 720" aria-hidden="true">
      <polygon points="0,0 420,0 420,60 170,250 0,120" fill="var(--charcoal-deep)"/>
      <polygon points="0,120 170,250 0,330" fill="var(--blue-light)"/>
      <polygon points="170,250 420,60 420,170 230,310" fill="var(--blue-deep)"/>
      <polygon points="0,330 170,250 230,310 420,440 420,540 0,260" fill="var(--blue)"/>
    </svg>

    <div class="back-brand">
      <p class="back-brand__name">VELMORAXIS</p>
      <p class="back-brand__web">velmoraxis.example</p>
    </div>
  </section>

</main>
</body>
</html>
```